New professional looking flyer for company

I need our flyer updated my flyer is the Lvb flyer Have attached current flyer so you know what services need to be listed. Want it to be in mainly dark colours like black and dark grey with pops of light grey, silver or white. i have added several photos for you to choose which ones work best with your design would like The photos to be in colour for the flyer. But can have a mix of greyscale if that works for your design j have attached another companies flyers as design ideas to show what I am looking for

Target Market(s)

new clients

Industry/Entity Type

transport and earthmoving

Colors

Designer to choose colors to be used in the design.

Requirements
Nice to have
• Look professional
Should not have
• No orange or red or green

```html
<!DOCTYPE html>
<html lang="en">
<head>
<meta charset="utf-8">
<title>Lvb Pty Ltd – Rentals, Sales and Services</title>
<link rel="stylesheet" href="https://fonts.googleapis.com/css2?family=Poppins:wght@400;500;600;700;800&display=swap">
<style>
  :root {
    --page-bg: #c3ccd8;
    --paper: #f4f4f3;
    --ink-dark: #262626;
    --ink-mid: #4a4a4a;
    --grey-band: #c9c9ca;
    --grey-box: #e3e3e5;
    --white: #ffffff;
    --tick: #555555;
  }
  * { margin: 0; padding: 0; box-sizing: border-box; }
  html, body {
    width: 1200px; height: 800px; overflow: hidden;
    background: var(--page-bg);
    font-family: "Poppins", sans-serif;
  }
  .flyer {
    position: absolute; left: 327px; top: 15px;
    width: 545px; height: 770px;
    background: var(--paper);
    overflow: hidden;
    box-shadow: 0 6px 20px rgba(40, 50, 70, .25);
  }
  .brand {
    position: absolute; left: 55px; top: 44px;
    display: flex; align-items: center; gap: 10px;
    font-weight: 800; font-size: 38px; color: var(--ink-dark);
    letter-spacing: 1px; line-height: 1;
  }
  .brand-mark { width: 18px; height: 18px; background: var(--ink-dark); }

  .hero-panel {
    position: absolute; inset: 0;
    background: var(--ink-dark);
    clip-path: polygon(0 100px, 305px 100px, 400px 380px, 378px 410px, 0 410px);
    z-index: 2;
  }
  .hero-photo {
    position: absolute; inset: 0;
    background: linear-gradient(180deg, #b7bcc8 0%, #a7a9a6 22%, #6f6f66 34%, #8d7363 52%, #91614c 75%, #7f5443 100%);
    clip-path: polygon(350px 40px, 545px 40px, 545px 380px, 418px 380px, 323px 100px, 375px 100px);
    z-index: 1;
  }
  .hero-copy {
    position: absolute; left: 40px; top: 160px; width: 330px;
    color: var(--white); z-index: 3;
  }
  .hero-title {
    font-weight: 800; font-size: 42px; line-height: 1.02; letter-spacing: .5px;
  }
  .hero-sub {
    margin-top: 6px; font-weight: 600; font-size: 13.5px; letter-spacing: .3px;
  }
  .hero-body {
    margin-top: 10px; font-size: 7.5px; line-height: 1.5; color: #d8d8d8; width: 300px;
  }

  .services-band {
    position: absolute; inset: 0;
    background: var(--grey-band);
    clip-path: polygon(418px 380px, 545px 380px, 545px 448px, 396px 448px, 410px 410px);
    z-index: 1;
  }
  .services-heading {
    position: absolute; right: 18px; top: 392px;
    font-weight: 700; font-size: 25px; color: var(--ink-mid); z-index: 3;
  }

  .services-box {
    position: absolute; left: 25px; top: 392px; width: 485px; height: 222px;
    background: var(--grey-box); border-radius: 14px; z-index: 0;
  }
  .service-list {
    position: absolute; list-style: none; z-index: 3;
    font-weight: 500; font-size: 13px; color: var(--ink-mid);
  }
  .service-list li { height: 22px; padding-left: 22px; position: relative; white-space: nowrap; }
  .service-list li::before {
    content: ""; position: absolute; left: 4px; top: 3px;
    width: 5px; height: 10px;
    border: solid var(--tick); border-width: 0 2px 2px 0;
    transform: rotate(40deg);
  }
  .service-list.primary { left: 40px; top: 425px; }
  .service-list.secondary { left: 300px; top: 470px; }

  .cta { position: absolute; left: 30px; top: 622px; width: 300px; z-index: 3; color: var(--ink-mid); }
  .cta-note { font-size: 9px; }
  .cta-line { margin-top: 3px; font-weight: 700; font-size: 16px; line-height: 1.2; color: var(--ink-dark); }

  .footer-base {
    position: absolute; inset: 0; background: var(--ink-dark);
    clip-path: polygon(0 690px, 240px 690px, 272px 770px, 0 770px);
    z-index: 2;
  }
  .footer-tail {
    position: absolute; inset: 0; background: #1f1f1f;
    clip-path: polygon(272px 770px, 300px 735px, 545px 700px, 545px 770px);
    z-index: 1;
  }
  .truck-photo {
    position: absolute; left: 300px; top: 605px; width: 245px; height: 145px;
    background: linear-gradient(160deg, #d9d4c6 0%, #b3ab98 30%, #3c3d44 55%, #2a2b30 80%, #6f6a60 100%);
    z-index: 1;
  }
  .contact { position: absolute; left: 22px; top: 698px; color: var(--white); z-index: 3; }
  .contact-phone { font-weight: 700; font-size: 22px; line-height: 1.1; }
  .contact-line { font-size: 9px; font-weight: 500; line-height: 1.4; }
</style>
</head>
<body>
  <main class="flyer">
    <div class="brand"><span class="brand-mark"></span>Lvb</div>

    <div class="hero-photo" role="img" aria-label="Photo of two road train prime movers with oversize signage on a red dirt yard"></div>
    <div class="hero-panel"></div>
    <div class="hero-copy">
      <h1 class="hero-title">RENTALS<br>SALES AND<br>SERVICES</h1>
      <p class="hero-sub">COMMERCIAL AND RESIDENTIAL</p>
      <p class="hero-body">Lorem Ipsum is simply dummy text of the printing and typesetting industry. Lorem Ipsum has been the industry's standard dummy text ever since the 1500s.</p>
    </div>

    <div class="services-box"></div>
    <div class="services-band"></div>
    <h2 class="services-heading">Our Services</h2>

    <ul class="service-list primary">
      <li>Over Size Loads / Hot Shot Loads</li>
      <li>Heavy Vehicle Recovery Services</li>
      <li>Potable Water Deliveries</li>
      <li>Road Building / Maintenance</li>
      <li>Earthworks</li>
      <li>Sand &amp; Metal Supply &amp; Cartages</li>
    </ul>
    <ul class="service-list secondary">
      <li>Road Train Tippers</li>
      <li>Road Train Tankers</li>
      <li>Road Train Flat Tops</li>
      <li>Drop Deck Trailers</li>
      <li>Mine Site accredited</li>
      <li>equipment &amp; Operators</li>
    </ul>

    <div class="cta">
      <p class="cta-note">We offer a wide range of services not listed so ask</p>
      <p class="cta-line">Call us today for a personalised<br>quote to suit your needs.</p>
    </div>

    <div class="truck-photo" role="img" aria-label="Photo of a dark road train prime mover hauling a transportable building"></div>
    <div class="footer-tail"></div>
    <div class="footer-base"></div>
    <div class="contact">
      <p class="contact-phone">040 555 0192</p>
      <p class="contact-line">Depot: Lot 41, Ridgeway Track<br>Dunmore Flats</p>
      <p class="contact-line">accounts@lvbhaulage.com.au</p>
    </div>
  </main>
</body>
</html>
```